New website

We ned to create a new website that reflects more who we are. We are delivering exclusive premium products to our customers and the current website does not reflect our products at all.
We believe in less is more and need a webpage that is clean yet professional and exclusive.

Target Market(s)

Dentistry

Industry/Entity Type

Dental

Number of Pages Required

5+ page

Font styles to use
Sans Serif

Colors

Designer to choose colors to be used in the design.

Requirements
Must have
• Picture gallery
• Nice structure
• Clean layout
Nice to have
• Light fonts
Should not have
• Any italic font styles

```html
<!DOCTYPE html>
<html lang="en">
<head>
<meta charset="utf-8">
<title>Brightora – Dental Products</title>
<link href="https://fonts.googleapis.com/css2?family=Questrial&family=Nunito+Sans:wght@600;700&display=swap" rel="stylesheet">
<style>
  :root {
    --navy: #0f426e;
    --blue: #1566ad;
    --red: #e8173e;
    --white: #ffffff;
    --text: #6b6b6b;
    --line: #d9dde3;
    --head-font: "Nunito Sans", sans-serif;
    --body-font: "Questrial", sans-serif;
  }
  * { margin: 0; padding: 0; box-sizing: border-box; }
  html, body { width: 682px; height: 1200px; overflow: hidden; background: var(--white); }
  body { position: relative; font-family: var(--body-font); color: var(--text); }
  .abs { position: absolute; }
  .line { display: block; text-align: justify; text-align-last: justify; }
  .line.last { text-align-last: left; }

  /* header */
  .site-header { position: absolute; left: 0; top: 0; width: 682px; height: 35px; background: var(--white); border-bottom: 1px solid #c9d3de; z-index: 2; }
  .brand { left: 75px; top: 7px; font-family: var(--head-font); font-weight: 700; font-size: 17px; color: var(--navy); }
  .main-nav a { position: absolute; top: 9px; height: 17px; line-height: 17px; font-family: var(--head-font); font-weight: 700; font-size: 10px; color: var(--blue); text-decoration: none; }
  .main-nav .is-active { background: var(--red); color: var(--white); padding: 0 7px; }

  /* hero */
  .hero { left: 0; top: 35px; width: 682px; height: 388px; background: var(--navy); overflow: hidden; }
  .hero-motif { left: -20px; top: 200px; width: 360px; height: 230px; border-radius: 50% 50% 0 0; background: radial-gradient(ellipse at 50% 90%, rgba(255,255,255,0.06), rgba(255,255,255,0.18) 60%, rgba(255,255,255,0) 72%); }
  .hero-title { left: 70px; top: 103px; font-family: var(--head-font); font-weight: 700; font-size: 38px; color: var(--white); }
  .hero-text { left: 75px; top: 177px; width: 319px; font-size: 9px; line-height: 13px; color: var(--white); }
  .slider-dots { display: flex; gap: 3px; }
  .slider-dots span { width: 6px; height: 6px; border-radius: 50%; background: var(--white); }
  .slider-dots span.on { background: var(--red); }
  .hero .slider-dots { left: 361px; top: 229px; }

  .appointment { left: 439px; top: 91px; width: 167px; height: 206px; background: var(--white); box-shadow: 0 2px 8px rgba(0,0,0,0.35); }
  .appointment h2 { height: 27px; line-height: 27px; text-align: center; font-family: var(--head-font); font-weight: 700; font-size: 13px; color: var(--blue); border-bottom: 1px solid var(--blue); }
  .field { position: absolute; left: 10px; width: 149px; height: 22px; border: 1px solid var(--line); font-size: 6px; color: #b5b9bf; padding: 7px 5px; }
  .check-btn { position: absolute; left: 10px; top: 163px; width: 149px; height: 22px; background: var(--red); color: var(--white); font-family: var(--head-font); font-weight: 700; font-size: 12px; text-align: center; line-height: 22px; border-bottom: 2px solid #b8102f; }

  /* features */
  .section-title { font-family: var(--head-font); font-weight: 700; color: var(--blue); text-align: center; }
  .best-title { left: 0; top: 460px; width: 682px; font-size: 15px; }
  .feature { top: 504px; width: 170px; height: 50px; }
  .feature-icon { position: absolute; left: 0; top: 0; width: 31px; height: 31px; background: linear-gradient(135deg, #f0355a, #d8123a); }
  .feature-icon svg { width: 31px; height: 31px; }
  .feature h3 { position: absolute; left: 36px; top: 0; font-weight: 400; font-size: 7.2px; color: var(--red); font-family: var(--body-font); }
  .feature p { position: absolute; left: 36px; top: 9px; width: 134px; font-size: 6.8px; line-height: 10.3px; }

  /* about */
  .offset-block { left: 166px; top: 755px; width: 227px; height: 211px; background: var(--blue); }
  .clinic-photo { left: 75px; top: 603px; width: 304px; height: 349px; background: linear-gradient(160deg, #e9edf6 0%, #cfd7e8 55%, #b9a99a 100%); }
  .about-title { left: 428px; top: 686px; font-family: var(--head-font); font-weight: 700; font-size: 27px; color: var(--blue); }
  .about-text { left: 428px; top: 730px; width: 172px; font-size: 7.3px; line-height: 10.3px; }
  .contact-btn { left: 457px; top: 778px; width: 149px; height: 23px; background: var(--blue); color: var(--white); font-family: var(--head-font); font-weight: 700; font-size: 12px; text-align: center; line-height: 23px; border-bottom: 2px solid #0d4f87; }

  /* testimonials & gallery */
  .testi-title { left: 105px; top: 1038px; width: 200px; font-size: 16px; }
  .gallery-title { left: 378px; top: 1038px; width: 200px; font-size: 16px; }
  .avatar { left: 75px; top: 1077px; width: 32px; height: 32px; border: 1px solid var(--blue); background: linear-gradient(180deg, #f3e3d6, #d9b99e); }
  .quote-name { left: 111px; top: 1077px; font-size: 7.2px; color: var(--red); }
  .quote-text { left: 111px; top: 1086px; width: 210px; font-size: 6.8px; line-height: 10.3px; }
  .gallery-photo { top: 1077px; width: 122px; height: 72px; }
  .gallery-photo.one { left: 348px; background: linear-gradient(120deg, #e3c2a8, #f1e7df 60%, #8fd4cc); }
  .gallery-photo.two { left: 484px; background: linear-gradient(120deg, #3a4c63, #dbe4ec 55%, #7fcfc6); }
  .small-dots { display: flex; gap: 2px; }
  .small-dots span { width: 3px; height: 3px; border-radius: 50%; background: #d0d0d0; }
  .small-dots span.on { background: var(--red); }
</style>
</head>
<body>
  <header class="site-header">
    <div class="brand abs">Brightora</div>
    <nav class="main-nav">
      <a class="is-active" style="left:393px">Home</a>
      <a style="left:443px">Products</a>
      <a style="left:499px">About Us</a>
      <a style="left:556px">Contact Us</a>
    </nav>
  </header>

  <section class="hero abs">
    <div class="hero-motif abs" role="img" aria-label="Faint line drawing of a tooth"></div>
    <h1 class="hero-title abs">We Create Smiles</h1>
    <p class="hero-text abs">
      <span class="line">Your natural teeth, you should try to nurture the best possible way.</span>
      <span class="line">They are the finest and most precious of chewing function created -</span>
      <span class="line">but they must also harmonize with your personality and appearance</span>
    </p>
    <div class="slider-dots abs"><span class="on"></span><span></span><span></span><span></span></div>
    <form class="appointment abs">
      <h2>Make An Appoinment</h2>
      <div class="field" style="top:49px">Full Name (Required)</div>
      <div class="field" style="top:87px">Email (Required)</div>
      <div class="field" style="top:126px">Phone (Required)</div>
      <div class="check-btn">CHECK</div>
    </form>
  </section>

  <h2 class="section-title best-title abs">What Makes Us Best</h2>

  <div class="feature abs" style="left:75px">
    <div class="feature-icon"><svg viewBox="0 0 31 31" fill="none" stroke="#fff" stroke-width="1.6"><circle cx="10" cy="8" r="3"/><path d="M10 11v14M21 6v10c0 3-3 3-3 6v3"/></svg></div>
    <h3>Technology</h3>
    <p><span class="line">Lorem Ipsum is simply dummy text of</span><span class="line">the printing and typesetting industry.</span><span class="line">Lorem Ipsum has been the industry's</span><span class="line last">standard gatype and scrambled it.</span></p>
  </div>
  <div class="feature abs" style="left:257px">
    <div class="feature-icon"><svg viewBox="0 0 31 31"><path d="M10 7c3 0 4 1.5 5.5 1.5S18 7 21 7c3 0 4 3 3 7-1 3-2 4-2 8 0 3-2 3-2.5 0L18 17c-.5-2-4.5-2-5 0l-1.5 6c-.5 3-2.5 3-2.5 0 0-4-1-5-2-8-1-4 0-8 3-8z" fill="#fff"/></svg></div>
    <h3>Services</h3>
    <p><span class="line">Lorem Ipsum is simply dummy text of</span><span class="line">the printing and typesetting industry.</span><span class="line">Lorem Ipsum has been the industry's</span><span class="line last">standard gatype and scrambled it.</span></p>
  </div>
  <div class="feature abs" style="left:439px">
    <div class="feature-icon"><svg viewBox="0 0 31 31" fill="none" stroke="#fff" stroke-width="1.8"><circle cx="15.5" cy="15.5" r="7"/><path d="M15.5 11.5v4.5h-3"/></svg></div>
    <h3>Availibilty</h3>
    <p><span class="line">Lorem Ipsum is simply dummy text of</span><span class="line">the printing and typesetting industry.</span><span class="line">Lorem Ipsum has been the industry's</span><span class="line last">standard gatype and scrambled it.</span></p>
  </div>

  <div class="offset-block abs"></div>
  <div class="clinic-photo abs" role="img" aria-label="Photo of a modern dental treatment room with a dental chair"></div>
  <h2 class="about-title abs">Lorem Ipsum</h2>
  <p class="about-text abs">There are many variations of passages of Lorem Ipsum available, but the majority have suffered alteration in some form, by injected humour</p>
  <div class="contact-btn abs">CONTACT US</div>

  <h2 class="section-title testi-title abs">Testimonials</h2>
  <h2 class="section-title gallery-title abs">Gallery</h2>

  <div class="avatar abs" role="img" aria-label="Photo of the reviewer"></div>
  <div class="quote-name abs">Mark Ellis</div>
  <p class="quote-text abs"><span class="line">Lorem ipsum dolor sit amet, consectetur adipiscing elit, sed</span><span class="line">do eiusmod tempor incididunt ut labore et dolore magna</span><span class="line last">aliqua. Ut enim ad minim veniam</span></p>
  <div class="small-dots abs" style="left:321px;top:1158px"><span class="on"></span><span></span><span></span></div>

  <div class="gallery-photo one abs" role="img" aria-label="Photo of a patient during a dental check-up"></div>
  <div class="gallery-photo two abs" role="img" aria-label="Photo of a dentist treating a patient"></div>
  <div class="small-dots abs" style="left:592px;top:1158px"><span class="on"></span><span></span><span></span></div>
</body>
</html>
```